DESIGN FOR TRADE SHOW FLOOR DISPLAY

March 25: I FORGOT TO INCLUDE THE OUTLINE OF WHAT I WANT FOR THE BOOTH. I JUST ADDED IT HERE. The document is called BOOTH DESIGN.

I need a design for a booth for trade shows. To see what I mean, please look at image 1 attached below.

The back wall part of the display shows graphics on the front of the display as well as the sides of the display.

I also need to have a design for the podium. See image 1 below.

I've attached the specifications for the designs.

The document for the back wall is called GRAPHIC TEMPLATE DESIGN FOR BACK WALL.

The document for the podium is called PODIUM TEMPLATE.

I've attached two other documents:

1. A large image of the cover of my book.

2. A copy of the Moorvale Financial logo.

I think this is everything that you will need. Please let me know if there is anything else that you need.

Thanks!

Ned Calloway

Target Market(s)

CPAs and accountants. Financial professionals.

Industry/Entity Type

Trade

Font styles to use
Other font styles liked:
• Use your best idea to worth with book cover and logo.

Requirements
Must have
• The colors and fonts work well with both the book cover and the Moorvale Financial logo.
• I've attached samples of booth designs that I like. They are called Sample 1, Sample 2, Sample 3, Sample 4. They are in no particular order.

```html
<!DOCTYPE html>
<html lang="en">
<head>
<meta charset="utf-8">
<title>Don't Say Nobody Warned You – Trade Show Back Wall</title>
<link rel="stylesheet" href="https://fonts.googleapis.com/css2?family=Bebas+Neue&family=Cinzel:wght@400;500&display=swap">
<style>
  :root {
    --brand-blue: #0b6bbb;
    --accent-cyan: #2cb7ea;
    --ink-black: #000000;
    --paper-white: #ffffff;
    --logo-navy: #143a66;
    --logo-green: #3fae49;
    --photo-dark: #0a1524;
    --photo-glow: #1e8fd8;
  }
  * { margin: 0; padding: 0; box-sizing: border-box; }
  html, body { width: 1200px; height: 792px; overflow: hidden; background: var(--paper-white); }
  .backwall { position: relative; width: 1200px; height: 792px; background: var(--paper-white); }
  .block { position: absolute; }
  .band-blue { background: var(--brand-blue); }
  .band-black { background: var(--ink-black); }
  .top-band { left: 0; top: 0; width: 1200px; height: 40px; }
  .bottom-band { left: 0; top: 760px; width: 1200px; height: 32px; }
  .cover-photo {
    left: 144px; top: 50px; width: 474px; height: 702px;
    background:
      radial-gradient(ellipse 60% 45% at 85% 40%, var(--photo-glow) 0%, rgba(30,143,216,0) 70%),
      linear-gradient(100deg, #1a1d22 0%, #23262b 40%, var(--photo-dark) 70%, #0c2a4a 100%);
  }
  .spine-left { left: 0; top: 50px; width: 144px; height: 548px; }
  .spine-right { left: 1056px; top: 50px; width: 144px; height: 548px; }
  .subtitle-band { left: 0; top: 606px; width: 618px; height: 70px; }
  .subtitle-band-right { left: 1054px; top: 606px; width: 146px; height: 70px; }
  .author-band { left: 0; top: 682px; width: 144px; height: 70px; }
  .author-band-right { left: 1056px; top: 682px; width: 144px; height: 70px; }
  .author-strip { left: 144px; top: 682px; width: 474px; height: 70px; background: rgba(0,0,0,0.82); }
  .alliance-panel { left: 618px; top: 50px; width: 438px; height: 702px; }
  .logo-plate { left: 618px; top: 606px; width: 436px; height: 70px; background: var(--paper-white); }
  .text-layer { position: absolute; left: 0; top: 0; }
  .title-line { font-family: "Bebas Neue", "Oswald", sans-serif; font-size: 117px; fill: var(--paper-white); }
  .title-line.accent { fill: var(--accent-cyan); }
  .spine-title { font-family: "Bebas Neue", sans-serif; font-size: 40px; fill: var(--paper-white); }
  .spine-title .accent { fill: var(--accent-cyan); }
  .spine-author { font-family: "Cinzel", serif; font-size: 30px; fill: var(--paper-white); }
  .subtitle { font-family: "Cinzel", serif; font-size: 31px; fill: var(--paper-white); }
  .author-name { font-family: "Cinzel", serif; font-size: 36px; fill: var(--paper-white); }
  .alliance-heading { font-family: "Bebas Neue", sans-serif; font-size: 44px; fill: var(--paper-white); }
  .benefit { font-family: "Bebas Neue", sans-serif; font-size: 34px; fill: var(--paper-white); }
  .benefit-dot { fill: var(--accent-cyan); }
  .company-name { font-family: "Bebas Neue", sans-serif; font-size: 30px; fill: var(--logo-navy); }
</style>
</head>
<body>
<main class="backwall">
  <div class="block band-blue top-band"></div>
  <div class="block cover-photo" role="img" aria-label="Author portrait: man in dark suit and patterned tie against a dark blue background"></div>
  <div class="block band-black spine-left"></div>
  <div class="block band-black spine-right"></div>
  <div class="block band-blue alliance-panel"></div>
  <div class="block band-blue subtitle-band"></div>
  <div class="block band-blue subtitle-band-right"></div>
  <div class="block band-black author-band"></div>
  <div class="block author-strip"></div>
  <div class="block band-black author-band-right"></div>
  <div class="block logo-plate"></div>
  <div class="block band-blue bottom-band"></div>

  <svg class="text-layer" width="1200" height="792" viewBox="0 0 1200 792">
    <!-- Left spine -->
    <g transform="translate(130 394) rotate(-90)">
      <text class="spine-title" x="0" y="0" textLength="290" lengthAdjust="spacingAndGlyphs">DON'T SAY NOBODY <tspan class="accent">WARNED YOU</tspan></text>
    </g>
    <line x1="98" y1="416" x2="142" y2="416" stroke="#333" stroke-width="1"/>
    <g transform="translate(126 582) rotate(-90)">
      <text class="spine-author" x="0" y="0" textLength="146" lengthAdjust="spacingAndGlyphs">NED CALLOWAY</text>
    </g>

    <!-- Right spine -->
    <g transform="translate(1106 394) rotate(-90)">
      <text class="spine-title" x="0" y="0" textLength="290" lengthAdjust="spacingAndGlyphs">DON'T SAY NOBODY <tspan class="accent">WARNED YOU</tspan></text>
    </g>
    <line x1="1076" y1="416" x2="1118" y2="416" stroke="#333" stroke-width="1"/>
    <g transform="translate(1102 582) rotate(-90)">
      <text class="spine-author" x="0" y="0" textLength="146" lengthAdjust="spacingAndGlyphs">NED CALLOWAY</text>
    </g>

    <!-- Cover title -->
    <g class="cover-title" text-anchor="end">
      <text class="title-line" x="590" y="214" textLength="134" lengthAdjust="spacingAndGlyphs">DON'T</text>
      <text class="title-line" x="590" y="304" textLength="96" lengthAdjust="spacingAndGlyphs">SAY</text>
      <text class="title-line" x="590" y="394" textLength="176" lengthAdjust="spacingAndGlyphs">NOBODY</text>
      <text class="title-line accent" x="590" y="484" textLength="176" lengthAdjust="spacingAndGlyphs">WARNED</text>
      <text class="title-line accent" x="590" y="574" textLength="96" lengthAdjust="spacingAndGlyphs">YOU</text>
    </g>

    <!-- Subtitle and author -->
    <g text-anchor="middle">
      <text class="subtitle" x="384" y="638" textLength="426" lengthAdjust="spacingAndGlyphs">A Straight-Talk Guide To</text>
      <text class="subtitle" x="384" y="667" textLength="250" lengthAdjust="spacingAndGlyphs">Lasting Wealth</text>
    </g>
    <text class="author-name" x="176" y="733" textLength="416" lengthAdjust="spacing">NED CALLOWAY</text>

    <!-- Alliance panel -->
    <line x1="618" y1="110" x2="1056" y2="110" stroke="var(--paper-white)" stroke-width="1"/>
    <g text-anchor="middle">
      <text class="alliance-heading" x="838" y="178" textLength="96" lengthAdjust="spacingAndGlyphs">JOIN OUR</text>
      <text class="alliance-heading" x="838" y="218" textLength="324" lengthAdjust="spacingAndGlyphs">STRATEGIC ALLIANCE PROGRAM</text>
    </g>
    <defs>
      <g id="benefit-marker">
        <circle class="benefit-dot" cx="0" cy="0" r="2"/>
        <circle class="benefit-dot" cx="9" cy="0" r="2"/>
        <circle class="benefit-dot" cx="0" cy="9" r="2"/>
        <circle class="benefit-dot" cx="9" cy="9" r="2"/>
      </g>
    </defs>
    <g class="benefits">
      <use href="#benefit-marker" x="669" y="277"/>
      <text class="benefit" x="698" y="294" textLength="312" lengthAdjust="spacingAndGlyphs">OFFER FINANCIAL PLANNING SERVICES</text>
      <use href="#benefit-marker" x="669" y="332"/>
      <text class="benefit" x="698" y="349" textLength="238" lengthAdjust="spacingAndGlyphs">INCREASE CLIENT RETENTION</text>
      <use href="#benefit-marker" x="669" y="387"/>
      <text class="benefit" x="698" y="404" textLength="305" lengthAdjust="spacingAndGlyphs">STRENGTHEN CLIENT RELATIONSHIPS</text>
      <use href="#benefit-marker" x="669" y="443"/>
      <text class="benefit" x="698" y="460" textLength="240" lengthAdjust="spacingAndGlyphs">INCREASE CLIENT REFERRALS</text>
      <use href="#benefit-marker" x="669" y="498"/>
      <text class="benefit" x="698" y="515" textLength="232" lengthAdjust="spacingAndGlyphs">ENHANCE YOUR REPUTATION</text>
      <use href="#benefit-marker" x="669" y="553"/>
      <text class="benefit" x="698" y="570" textLength="237" lengthAdjust="spacingAndGlyphs">EARN ONGOING ANNUAL FEES</text>
    </g>

    <!-- Company name -->
    <rect x="710" y="629" width="24" height="24" fill="var(--logo-green)"/>
    <text class="company-name" x="746" y="652">MOORVALE FINANCIAL</text>
  </svg>
</main>
</body>
</html>
```